Tallow Ridge Advisory WordPress Site.

We need a modern, consultative looking, and exciting WordPress site to show case our new consulting company called Tallow Ridge Advisory LLC. Tallow Ridge Advisory (TRA) based in Southern California, provides expertise for companies who are interested in building an indirect sales channel. Some may think of this as building a Partner Program. Our offerings include, Discovery, Strategic Planning, Goals and Objective Setting, Partner Recruitment & Enablement, Team Building, and Outcome Definition. We purchased our logo from Fernquill which is attached. The colors are Blue and Grey. The final design should convey a fresh, modern, and exciting look. Don't forget this is a consulting company, so we can't get too "wild". Hopefully we can come up with a nice balance. We attached our logo (two versions) and our Founder's photo. Please let us know what else you need to get started. I suspect you'll outline the design and we can iterate on the copy. Lastly, we'll be using Brookvane as our hosting provider.

Target Market(s)

Small to mid-size SaaS Companies.

Industry/Entity Type

Consulting for Indirect Sales Channels

Coding

Coded - Design and coding required

Font styles to use
Other font styles liked:
• Please select a font that compliments the logo. Modern and easy to read.

Colors
0054AA
0677BA
7BADD7
CADEEF
E8F1F8
00AB8E
00BBA5
67D7C9
C6EFE9
E9F9F6
FFF300
FFF600
FEFA6F
FFFEC7
FFFEE8

Requirements
Must have
• My project must include the following pages. Homepage, About Us, Offerings & Services, and Contact Us
Nice to have
• Clean, bright and modern look. Area(s) and ability to insert video or blog posts.
Should not have
• Should not contain clutter. Black background.

```html
<!DOCTYPE html>
<html lang="en">
<head>
<meta charset="utf-8">
<title>Tallow Ridge Advisory</title>
<link href="https://fonts.googleapis.com/css2?family=Krona+One&family=Roboto:ital,wght@0,400;0,500;0,700;1,400&display=swap" rel="stylesheet">
<style>
:root{
  --blue:#0b3d9c;
  --blue-deep:#08307f;
  --grey-band:#8d8d8d;
  --ink:#1b1b1b;
  --muted:#7a7a7a;
  --line:#e3e3e3;
  --footer:#202020;
  --star:#f2b01e;
  --white:#ffffff;
}
*{margin:0;padding:0;box-sizing:border-box}
html,body{width:1200px;height:3481px;overflow:hidden}
body{font-family:'Roboto',sans-serif;color:var(--ink);background:var(--white);position:relative}
.display{font-family:'Krona One',sans-serif;letter-spacing:1px;text-transform:uppercase}
.section-title{position:absolute;left:0;width:1200px;text-align:center;font-size:25px}

/* header */
.topbar{position:absolute;top:0;left:0;width:1200px;height:8px;background:linear-gradient(90deg,var(--blue) 0 52%,#9a9a9a 52% 100%)}
.header{position:absolute;top:8px;left:0;width:1200px;height:87px;background:var(--white)}
.brand{position:absolute;left:111px;top:24px;display:flex;align-items:center;gap:10px;font-weight:500;font-size:19px;color:var(--blue)}
.brand-dot{width:26px;height:26px;border-radius:50%;background:var(--blue)}
.nav a{position:absolute;top:33px;font-size:15px;font-weight:500;color:var(--ink);text-decoration:none}
.nav a.active{color:var(--blue)}
.call-icon{position:absolute;left:862px;top:24px;width:36px;height:36px;border-radius:50%;background:var(--blue);display:flex;align-items:center;justify-content:center}
.call-label{position:absolute;left:919px;top:24px;font-size:13px;font-weight:500}
.call-number{position:absolute;left:919px;top:40px;font-size:21px;font-weight:700;color:var(--blue)}

/* hero */
.hero{position:absolute;top:95px;left:0;width:1200px;height:600px;background:linear-gradient(180deg,#dde5ee 0%,#c3d0de 55%,#8fa4b9 100%)}
.hero-fade{position:absolute;inset:0;background:linear-gradient(90deg,rgba(255,255,255,.55) 0%,rgba(255,255,255,.25) 45%,rgba(255,255,255,0) 70%)}
.hero-portrait{position:absolute;left:594px;top:0;width:554px;height:600px;background:linear-gradient(180deg,#b9a18f 0%,#5b4b44 45%,#1e1c1d 100%)}
.hero-title{position:absolute;left:111px;top:170px;font-size:43px;line-height:48px;color:var(--ink);white-space:nowrap}
.hero-sub{position:absolute;left:111px;top:290px;width:470px;font-size:19px;font-weight:500;line-height:28px}
.btn{position:absolute;display:flex;align-items:center;justify-content:center;gap:9px;background:var(--blue);color:var(--white);font-size:14px;font-weight:700;text-transform:uppercase;border-radius:3px}
.btn-dot{width:13px;height:13px;border-radius:50%;background:var(--white);position:relative}
.btn-dot::after{content:"";position:absolute;left:4px;top:3.5px;border-left:5px solid var(--blue);border-top:3px solid transparent;border-bottom:3px solid transparent}

/* story */
.story-frame{position:absolute;left:122px;top:866px;width:443px;height:445px;background:var(--blue);border-radius:14px}
.story-photo{position:absolute;left:115px;top:857px;width:438px;height:443px;border-radius:12px;background:linear-gradient(135deg,#e9ecef 0%,#c9ccd1 50%,#8c8f95 100%);border:3px solid var(--white)}
.step{position:absolute;left:630px;width:448px}
.step-badge{width:55px;height:29px;border-radius:15px;background:var(--blue);color:var(--white);font-size:16px;font-weight:500;display:flex;align-items:center;justify-content:center;margin-bottom:10px}
.step-badge.alt{background:#999}
.step p{font-size:14px;line-height:21.5px;color:var(--muted);text-align:justify}

/* offer */
.offer-grey{position:absolute;top:1432px;left:0;width:1200px;height:455px;background:linear-gradient(180deg,#8b8b8b,#a2a2a2)}
.offer-blue{position:absolute;top:1887px;left:0;width:1200px;height:548px;background:linear-gradient(180deg,#0d44ad 0%,#0b3c9a 60%,#0a3588 100%)}
.offer-card{position:absolute;width:234px;height:196px;border-radius:12px;background:rgba(255,255,255,.55)}
.offer-inner{position:absolute;left:13px;right:13px;top:16px;bottom:3px;border-radius:10px;background:var(--white);display:flex;flex-direction:column;align-items:center}
.offer-inner svg{margin-top:22px}
.offer-inner span{position:absolute;top:124px;font-size:17px;font-weight:500}

/* testimonials */
.tcard{position:absolute;top:2135px;width:469px;height:221px;background:var(--white);border-radius:14px}
.quote{position:absolute;left:32px;top:32px}
.stars{position:absolute;right:32px;top:33px;display:flex;gap:3px}
.tcard p{position:absolute;left:32px;top:70px;width:408px;font-size:14px;font-style:italic;line-height:24px;color:var(--muted)}
.avatar{position:absolute;left:32px;top:150px;width:44px;height:44px;border-radius:50%;background:linear-gradient(180deg,#d8d8d8,#9a9a9a)}
.tname{position:absolute;left:95px;top:156px;font-size:12px;font-weight:500;color:var(--blue);text-transform:uppercase}
.trole{position:absolute;left:95px;top:173px;font-size:12px;color:var(--blue)}
.arrow{position:absolute;top:2232px;width:38px;height:26px;background:var(--white);border-radius:3px;display:flex;align-items:center;justify-content:center}

/* news */
.news-photo{position:absolute;top:2605px;width:315px;height:208px;background:linear-gradient(160deg,#d9dde2 0%,#9aa2ad 55%,#4a4f58 100%)}
.news-card{position:absolute;top:2784px;width:282px;height:161px;background:var(--white);box-shadow:0 2px 10px rgba(0,0,0,.16)}
.news-date{position:absolute;left:25px;top:-12px;height:23px;padding:0 15px;background:var(--blue);color:var(--white);font-size:13px;font-weight:500;display:flex;align-items:center}
.news-card h3{position:absolute;left:28px;top:38px;font-size:15.5px;font-weight:500}
.news-rule{position:absolute;left:28px;top:67px;width:26px;height:2px;background:var(--blue)}
.news-card p{position:absolute;left:28px;top:84px;width:228px;font-size:12.5px;line-height:17px;color:var(--muted);text-align:justify}

/* footer */
.footer{position:absolute;top:3047px;left:0;width:1200px;height:434px;background:var(--footer)}
.contact-item{position:absolute;top:70px;width:240px;margin-left:-120px;text-align:center;color:var(--white)}
.contact-ring{width:86px;height:86px;margin:0 auto;border-radius:50%;border:2px dotted #1f4fb0;display:flex;align-items:center;justify-content:center}
.contact-icon{width:74px;height:74px;border-radius:50%;background:var(--blue);display:flex;align-items:center;justify-content:center}
.contact-item .label{margin-top:24px;font-size:12.5px;font-weight:700;text-transform:uppercase;line-height:18px}
.contact-item .value{font-size:14px;line-height:22px}
.contact-item .first{margin-top:24px}
.foot-brand{position:absolute;left:111px;top:275px;display:flex;align-items:center;gap:12px;color:var(--white);font-size:24px;font-weight:500}
.foot-brand .brand-dot{width:34px;height:34px;background:var(--white)}
.foot-nav{position:absolute;left:455px;top:285px;width:635px;display:flex;justify-content:space-between;color:var(--white);font-size:16px;font-weight:500}
.foot-rule{position:absolute;left:455px;top:326px;width:635px;height:1px;background:#4a4a4a}
.social{position:absolute;top:347px;display:flex;gap:7px;left:455px}
.social span{width:36px;height:36px;border-radius:50%;border:1px solid #bdbdbd}
.copy{position:absolute;right:112px;top:357px;font-size:14px;color:var(--white)}
</style>
</head>
<body>

<div class="topbar"></div>
<header class="header">
  <div class="brand"><span class="brand-dot"></span>Tallow Ridge Advisory</div>
  <nav class="nav">
    <a class="active" style="left:389px">Home</a>
    <a style="left:468px">About Us</a>
    <a style="left:568px">Our Services</a>
    <a style="left:691px">Blog</a>
    <a style="left:761px">Contact</a>
  </nav>
  <div class="call-icon"><svg width="18" height="18" viewBox="0 0 24 24"><path fill="#fff" d="M6.6 10.8a15.2 15.2 0 0 0 6.6 6.6l2.2-2.2c.3-.3.7-.4 1-.2 1.1.4 2.3.6 3.6.6.6 0 1 .4 1 1V20c0 .6-.4 1-1 1A17 17 0 0 1 3 4c0-.6.4-1 1-1h3.5c.6 0 1 .4 1 1 0 1.3.2 2.5.6 3.6.1.3 0 .7-.2 1z"/></svg></div>
  <div class="call-label">Call Us Today !</div>
  <div class="call-number">+ 1 555 014 2280</div>
</header>

<section class="hero">
  <div class="hero-fade"></div>
  <div class="hero-portrait" role="img" aria-label="Portrait of the company founder in a dark blazer"></div>
  <h1 class="hero-title display">Control Your<br>Future</h1>
  <p class="hero-sub">Create. Optimize. Unleash the Power of Partnerships &amp;Alliances.</p>
  <div class="btn" style="left:112px;top:374px;width:163px;height:47px">Get Started <span class="btn-dot"></span></div>
</section>

<h2 class="section-title display" style="top:770px">Our Story</h2>
<div class="story-frame"></div>
<div class="story-photo" role="img" aria-label="Two colleagues reviewing documents at an office desk"></div>
<div class="step" style="top:848px"><div class="step-badge">01</div><p>Do you worry about how you're going to make your revenue number while managing costs? You're not alone. Most business leaders wrestle with the same concern.</p></div>
<div class="step" style="top:973px"><div class="step-badge alt">02</div><p>What options do you have? You can hire more salespeople and business development reps. You can invest in Brightpath Ads, marketing campaigns, purchase lead lists, conduct webinars, increase social marketing, train your sales team, add solution engineers, etc. You get the picture</p></div>
<div class="step" style="top:1139px"><div class="step-badge">03</div><p>Have you considered scaling your business through partnerships and alliances? Do you really know what that means? Does your strategic plan include a robust indirect sales channel? If not, it should</p></div>
<div class="btn" style="left:630px;top:1270px;width:163px;height:47px">Learn More <span class="btn-dot"></span></div>

<div class="offer-grey"></div>
<div class="offer-blue"></div>
<h2 class="section-title display" style="top:1502px;color:#fff">What We Offer</h2>

<div class="offer-card" style="left:112px;top:1567px"><div class="offer-inner">
  <svg width="70" height="70" viewBox="0 0 70 70"><circle cx="42" cy="27" r="19" fill="none" stroke="#0b3d9c" stroke-width="6"/><path d="M28 41 8 62" stroke="#0b3d9c" stroke-width="8" stroke-linecap="round"/></svg>
  <span>Discovery</span></div></div>
<div class="offer-card" style="left:360px;top:1567px"><div class="offer-inner">
  <svg width="70" height="70" viewBox="0 0 70 70"><circle cx="28" cy="26" r="10" fill="none" stroke="#0b3d9c" stroke-width="6"/><circle cx="50" cy="18" r="6" fill="#0b3d9c"/><circle cx="52" cy="34" r="4" fill="#0b3d9c"/><path d="M8 50h20l14 6 20-10v8L40 64H8z" fill="#0b3d9c"/></svg>
  <span>Strategic Planning</span></div></div>
<div class="offer-card" style="left:607px;top:1567px"><div class="offer-inner">
  <svg width="70" height="70" viewBox="0 0 70 70"><circle cx="33" cy="36" r="26" fill="none" stroke="#0b3d9c" stroke-width="6"/><circle cx="33" cy="36" r="14" fill="none" stroke="#0b3d9c" stroke-width="5"/><circle cx="33" cy="36" r="4" fill="#0b3d9c"/><path d="M33 36 58 11" stroke="#0b3d9c" stroke-width="4"/></svg>
  <span>Goals &amp; Objective</span></div></div>
<div class="offer-card" style="left:854px;top:1567px"><div class="offer-inner">
  <svg width="70" height="70" viewBox="0 0 70 70"><rect x="20" y="6" width="38" height="52" rx="4" fill="none" stroke="#0b3d9c" stroke-width="5"/><path d="M42 22h10M42 32h10M42 42h10" stroke="#0b3d9c" stroke-width="4"/><circle cx="26" cy="38" r="12" fill="#fff" stroke="#0b3d9c" stroke-width="5"/><path d="M17 47 7 58" stroke="#0b3d9c" stroke-width="6" stroke-linecap="round"/></svg>
  <span>Partner Recruitment</span></div></div>
<div class="offer-card" style="left:235px;top:1790px"><div class="offer-inner">
  <svg width="70" height="70" viewBox="0 0 70 70"><rect x="4" y="12" width="62" height="48" rx="5" fill="#0b3d9c"/><path d="M14 24h42M14 36h42M14 48h42" stroke="#fff" stroke-width="3"/><circle cx="42" cy="24" r="4" fill="#0b3d9c" stroke="#fff" stroke-width="3"/><circle cx="26" cy="36" r="4" fill="#0b3d9c" stroke="#fff" stroke-width="3"/><circle cx="36" cy="48" r="4" fill="#0b3d9c" stroke="#fff" stroke-width="3"/></svg>
  <span>Enablement</span></div></div>
<div class="offer-card" style="left:482px;top:1790px"><div class="offer-inner">
  <svg width="70" height="70" viewBox="0 0 70 70"><circle cx="35" cy="30" r="22" fill="none" stroke="#0b3d9c" stroke-width="5" stroke-dasharray="6 4"/><circle cx="35" cy="24" r="7" fill="#0b3d9c"/><circle cx="18" cy="32" r="5" fill="#0b3d9c"/><circle cx="52" cy="32" r="5" fill="#0b3d9c"/><path d="M14 56c4-14 38-14 42 0z" fill="#0b3d9c"/></svg>
  <span>Team Building</span></div></div>
<div class="offer-card" style="left:730px;top:1790px"><div class="offer-inner">
  <svg width="70" height="70" viewBox="0 0 70 70"><rect x="14" y="8" width="42" height="56" rx="5" fill="#0b3d9c"/><rect x="26" y="4" width="18" height="9" rx="2" fill="#0b3d9c" stroke="#fff" stroke-width="2"/><path d="M20 24l3 3 5-5M20 37l3 3 5-5M20 50l3 3 5-5M32 25h16M32 38h16M32 51h16" stroke="#fff" stroke-width="3" fill="none"/></svg>
  <span>Outcome Definition</span></div></div>

<h2 class="section-title display" style="top:2057px;color:#fff">Testimonials</h2>
<div class="arrow" style="left:38px"><svg width="22" height="12" viewBox="0 0 22 12"><path d="M21 6H3M7 1 2 6l5 5" stroke="#111" stroke-width="2.4" fill="none"/></svg></div>
<div class="arrow" style="left:1124px"><svg width="22" height="12" viewBox="0 0 22 12"><path d="M1 6h18M15 1l5 5-5 5" stroke="#111" stroke-width="2.4" fill="none"/></svg></div>

<div class="tcard" style="left:113px">
  <svg class="quote" width="30" height="22" viewBox="0 0 30 22"><path d="M0 22V11C0 4 4 0 11 0v5c-3 0-5 2-5 5h5v12zM17 22V11c0-7 4-11 11-11v5c-3 0-5 2-5 5h5v12z" fill="#0b3d9c"/></svg>
  <div class="stars"><svg width="82" height="14" viewBox="0 0 82 14"><g fill="#f2b01e"><path id="s" d="M7 0l2 4.6 5 .5-3.8 3.3 1.1 5L7 11l-4.3 2.4 1.1-5L0 5.1l5-.5z"/><use href="#s" x="17"/><use href="#s" x="34"/><use href="#s" x="51"/><use href="#s" x="68"/></g></svg></div>
  <p>Lorem ipsum dolor sit amet, consectetur adipiscing elit, sed do eiusmod tempor incididunt ut labore et dolore magna aliqua. Ut enim ad minim veniam, quis nostrud exercitation</p>
  <div class="avatar" role="img" aria-label="Client headshot"></div>
  <div class="tname">John Doe</div><div class="trole">Businessman</div>
</div>
<div class="tcard" style="left:619px">
  <svg class="quote" width="30" height="22" viewBox="0 0 30 22"><path d="M0 22V11C0 4 4 0 11 0v5c-3 0-5 2-5 5h5v12zM17 22V11c0-7 4-11 11-11v5c-3 0-5 2-5 5h5v12z" fill="#0b3d9c"/></svg>
  <div class="stars"><svg width="82" height="14" viewBox="0 0 82 14"><g fill="#f2b01e"><use href="#s"/><use href="#s" x="17"/><use href="#s" x="34"/><use href="#s" x="51"/><use href="#s" x="68"/></g></svg></div>
  <p>Lorem ipsum dolor sit amet, consectetur adipiscing elit, sed do eiusmod tempor incididunt ut labore et dolore magna aliqua. Ut enim ad minim veniam, quis nostrud exercitation</p>
  <div class="avatar" role="img" aria-label="Client headshot"></div>
  <div class="tname">John Doe</div><div class="trole">Businessman</div>
</div>

<h2 class="section-title display" style="top:2512px">Latest News</h2>
<div class="news-photo" style="left:107px" role="img" aria-label="Colleagues discussing paperwork at a meeting table"></div>
<div class="news-photo" style="left:443px" role="img" aria-label="Team gathered around a conference table"></div>
<div class="news-photo" style="left:778px" role="img" aria-label="Business people smiling during a meeting"></div>
<div class="news-card" style="left:123px"><div class="news-date">Oct 2022</div><h3>Lorem ipsum dolor sit amet</h3><div class="news-rule"></div><p>Sed ut perspiciatis unde omnis iste natus error sit voluptatem accusantium doloremque laudantium</p></div>
<div class="news-card" style="left:459px"><div class="news-date">Oct 2022</div><h3>Lorem ipsum dolor sit amet</h3><div class="news-rule"></div><p>Sed ut perspiciatis unde omnis iste natus error sit voluptatem accusantium doloremque laudantium</p></div>
<div class="news-card" style="left:794px"><div class="news-date">Oct 2022</div><h3>Lorem ipsum dolor sit amet</h3><div class="news-rule"></div><p>Sed ut perspiciatis unde omnis iste natus error sit voluptatem accusantium doloremque laudantium</p></div>

<footer class="footer">
  <div class="contact-item" style="left:232px">
    <div class="contact-ring"><div class="contact-icon"><svg width="20" height="26" viewBox="0 0 20 26"><path d="M10 0a10 10 0 0 0-10 10c0 7 10 16 10 16s10-9 10-16A10 10 0 0 0 10 0zm0 14a4 4 0 1 1 0-8 4 4 0 0 1 0 8z" fill="#fff"/></svg></div></div>
    <div class="value first">4180 Marlow Terrace<br>Southern California</div>
  </div>
  <div class="contact-item" style="left:476px">
    <div class="contact-ring"><div class="contact-icon"><svg width="28" height="20" viewBox="0 0 28 20"><rect x="1.5" y="1.5" width="25" height="17" rx="2" fill="none" stroke="#fff" stroke-width="2.5"/><path d="M2 3l12 9 12-9" fill="none" stroke="#fff" stroke-width="2.5"/></svg></div></div>
    <div class="label">Email Address</div><div class="value">info@tallowridge.com</div>
  </div>
  <div class="contact-item" style="left:720px">
    <div class="contact-ring"><div class="contact-icon"><svg width="24" height="24" viewBox="0 0 24 24"><path fill="#fff" d="M6.6 10.8a15.2 15.2 0 0 0 6.6 6.6l2.2-2.2c.3-.3.7-.4 1-.2 1.1.4 2.3.6 3.6.6.6 0 1 .4 1 1V20c0 .6-.4 1-1 1A17 17 0 0 1 3 4c0-.6.4-1 1-1h3.5c.6 0 1 .4 1 1 0 1.3.2 2.5.6 3.6.1.3 0 .7-.2 1z"/></svg></div></div>
    <div class="label">Phone No</div><div class="value">+ 1 555 014 2280</div>
  </div>
  <div class="contact-item" style="left:963px">
    <div class="contact-ring"><div class="contact-icon"><svg width="26" height="26" viewBox="0 0 26 26"><rect x="2" y="8" width="22" height="16" rx="2" fill="#fff"/><rect x="7" y="2" width="12" height="8" fill="#fff"/><rect x="6" y="12" width="4" height="9" fill="#0b3d9c"/><path d="M13 13h2M17 13h2M13 17h2M17 17h2M13 21h2M17 21h2" stroke="#0b3d9c" stroke-width="2"/></svg></div></div>
    <div class="label">Fax</div><div class="value">+ 1 555 014 2291</div>
  </div>

  <div class="foot-brand"><span class="brand-dot"></span>Tallow Ridge Advisory</div>
  <nav class="foot-nav"><span>Home</span><span>|</span><span>About Us</span><span>|</span><span>Our Services</span><span>|</span><span>Blog</span><span>|</span><span>Contact</span></nav>
  <div class="foot-rule"></div>
  <div class="social"><span aria-label="Social link"></span><span aria-label="Social link"></span><span aria-label="Social link"></span></div>
  <div class="copy">© 2022 Tallow Ridge Advisory. All Right Reserved.</div>
</footer>

</body>
</html>
```